Tolvik cards

I want a simple business card that pops.
Logo on one side.
On side two i want.
"Are you thinking about a new building on your property, or renovating an existing structure? Contact".....
Owners Name: Gary Pellman
Owners Phone number: 555-209-4176
Address:4716 Copper Fern RD, Linden Hollow, PA 16980
Committed to Quality, Service, and Integrity

```html
<!DOCTYPE html>
<html lang="en">
<head>
<meta charset="utf-8">
<title>Tolvik Builders – Business Card</title>
<link href="https://fonts.googleapis.com/css2?family=Montserrat:wght@400;500;700;800;900&display=swap" rel="stylesheet">
<style>
  :root {
    --page-bg: #f1f1f1;
    --brown-dark: #3f2d1d;
    --brown-line: #7a5a3b;
    --card-white: #ffffff;
    --ink: #2e1f12;
    --ink-soft: #3a2a1c;
  }
  * { margin: 0; padding: 0; box-sizing: border-box; }
  html, body { width: 1200px; height: 800px; overflow: hidden; }
  body {
    background: var(--page-bg);
    font-family: "Montserrat", Arial, sans-serif;
    display: flex;
    flex-direction: column;
    align-items: center;
    justify-content: center;
    gap: 40px;
  }
  .card {
    width: 600px;
    height: 343px;
    position: relative;
    box-shadow: 0 6px 18px rgba(0,0,0,0.18);
  }

  /* Front */
  .card-front { background: var(--brown-dark); overflow: hidden; }
  .front-pattern {
    position: absolute; inset: 0;
    background: linear-gradient(135deg, #46331f 0%, #3f2d1d 50%, #3a2919 100%);
  }
  .logo-frame {
    position: absolute;
    left: 125px; top: 96px;
    width: 350px; height: 150px;
    border: 4px solid var(--brown-line);
    background: var(--brown-dark);
    display: flex; align-items: center; justify-content: center; gap: 12px;
  }
  .logo-square { flex: none; width: 24px; height: 24px; background: var(--card-white); }
  .logo-name {
    color: var(--card-white);
    font-weight: 900;
    font-size: 19px;
    letter-spacing: 0.5px;
    text-transform: uppercase;
    line-height: 1;
    white-space: nowrap;
  }

  /* Back */
  .card-back { background: var(--card-white); color: var(--ink); }
  .question {
    position: absolute;
    right: 325px; top: 86px;
    width: 200px;
    text-align: right;
    font-weight: 800;
    font-size: 12px;
    line-height: 1.4;
    letter-spacing: 0.6px;
    text-transform: uppercase;
  }
  .divider {
    position: absolute;
    left: 292px; top: 78px;
    width: 5px; height: 190px;
    background: var(--ink);
  }
  .contact { position: absolute; left: 322px; top: 118px; }
  .contact-label { font-weight: 800; font-size: 17px; letter-spacing: 0.5px; text-transform: uppercase; }
  .contact-name { font-weight: 400; font-size: 21px; margin-top: 2px; }
  .contact-line {
    display: flex; align-items: flex-start; gap: 10px;
    font-size: 12px; letter-spacing: 1px; color: var(--ink-soft);
    margin-top: 14px; line-height: 1.35;
  }
  .contact-line svg { flex: none; width: 14px; height: 14px; fill: var(--ink); margin-top: 1px; }
  .tagline {
    position: absolute;
    left: 0; right: 0; bottom: 30px;
    text-align: center;
    font-weight: 800;
    font-size: 11px;
    letter-spacing: 2px;
    text-transform: uppercase;
  }
</style>
</head>
<body>
  <section class="card card-front">
    <div class="front-pattern" role="img" aria-label="Decorative geometric line pattern in light brown on dark brown"></div>
    <div class="logo-frame">
      <span class="logo-square"></span>
      <span class="logo-name">Tolvik Builders LLC</span>
    </div>
  </section>

  <section class="card card-back">
    <p class="question">Are you thinking<br>about a new building<br>on your property,<br>or renovating an<br>existing structure?</p>
    <div class="divider"></div>
    <div class="contact">
      <p class="contact-label">Contact</p>
      <p class="contact-name">Gary Pellman</p>
      <p class="contact-line">
        <svg viewBox="0 0 24 24" aria-hidden="true"><path d="M6.6 10.8a15.1 15.1 0 0 0 6.6 6.6l2.2-2.2c.3-.3.7-.4 1-.2 1.1.4 2.300.6 3.6.6.6 0 1 .4 1 1V20c0 .6-.4 1-1 1A17 17 0 0 1 3 4c0-.6.4-1 1-1h3.5c.6 0 1 .4 1 1 0 1.3.2 2.500.6 3.6.1.3 0 .7-.2 1z"/></svg>
        <span>555-209-4176</span>
      </p>
      <p class="contact-line">
        <svg viewBox="0 0 24 24" aria-hidden="true"><path d="M12 2a7 7 0 0 0-7 7c0 5.2 7 13 7 13s7-7.8 7-13a7 7 0 0 0-7-7zm0 9.5A2.5 2.5 0 1 1 12 6.5a2.5 2.5 0 0 1 0 5z"/></svg>
        <span>4716 Copper Fern RD,<br>Linden Hollow, PA 16980</span>
      </p>
    </div>
    <p class="tagline">Committed to Quality, Service, and Integrity</p>
  </section>
</body>
</html>
```